Consulting company with focus on aviation needs

We need a new business card design for our company. The company consults with multiple players in the industry like manufacturers and airlines. It is also a supplier and an inter-company level. Given the targeted industry (aviation) it should be both kind of serious, sound, secure, classy, ​​but also a bit technical, innovative. Should not be too playful, however, "fresh", "airy", "ligth" and "suprising" are suitabe attributes. The existing logo shall be used.

Airlines

```html
<!DOCTYPE html>
<html lang="en">
<head>
<meta charset="utf-8">
<title>VELIRO Business Card</title>
<link href="https://fonts.googleapis.com/css2?family=Questrial&family=Saira:wght@500&display=swap" rel="stylesheet">
<style>
  :root {
    --page: #ffffff;
    --frame: #111111;
    --card: #f1f7f7;
    --card-edge: #d3d9d9;
    --pattern-light: #f8fbfb;
    --pattern-soft: #e7f0f0;
    --ink: #5b5650;
    --accent: #f08a00;
    --link: #1b8a95;
    --mark: #3a9068;
  }
  * { box-sizing: border-box; margin: 0; padding: 0; }
  html, body { width: 1054px; height: 1200px; overflow: hidden; background: var(--page); }
  .canvas {
    position: relative; width: 1054px; height: 1200px;
    border: 1px solid var(--frame); background: var(--page);
  }
  .card {
    position: absolute; left: 131px; width: 792px; height: 453px;
    background: var(--card); border: 1px solid var(--card-edge); overflow: hidden;
  }
  .card--front { top: 102px; }
  .card--back { top: 642px; }
  .card__pattern {
    position: absolute; inset: 0;
    background:
      radial-gradient(circle at 88% 30%, var(--pattern-soft) 0, transparent 38%),
      radial-gradient(circle at 82% 75%, var(--pattern-light) 0, transparent 30%),
      linear-gradient(120deg, var(--pattern-light) 0%, var(--card) 55%, var(--pattern-soft) 100%);
  }
  .brand-dot { position: absolute; border-radius: 50%; background: var(--mark); }
  .brand-name {
    position: absolute; font-family: "Questrial", sans-serif; color: var(--ink);
    letter-spacing: 0.5em; line-height: 1; white-space: nowrap;
  }
  .tagline {
    position: absolute; font-family: "Saira", sans-serif; font-weight: 500;
    color: var(--accent); line-height: 1; white-space: nowrap;
  }
  /* front */
  .card--front .brand-dot { left: 338px; top: 108px; width: 116px; height: 116px; }
  .card--front .brand-name { left: 0; width: 792px; text-align: center; top: 248px; font-size: 54px; padding-left: 0.5em; }
  .card--front .tagline { left: 0; width: 792px; text-align: center; top: 300px; font-size: 21px; }
  /* back */
  .card--back .brand-dot { left: 58px; top: 47px; width: 80px; height: 80px; }
  .card--back .brand-name { left: 154px; top: 60px; font-size: 34px; }
  .card--back .tagline { left: 154px; top: 96px; font-size: 15px; }
  .person { position: absolute; left: 58px; top: 214px; font-family: "Questrial", sans-serif; color: var(--ink); }
  .person__name { font-size: 38px; line-height: 1; }
  .person__role { font-size: 20px; margin-top: 6px; }
  .contact {
    position: absolute; left: 58px; top: 306px; list-style: none;
    font-family: "Questrial", sans-serif; font-size: 19px; color: var(--ink); line-height: 24px;
  }
  .contact li { display: flex; }
  .contact__label { width: 87px; }
  .contact__value::before { content: ":"; margin-right: 7px; }
  .contact__value--link { color: var(--link); }
  .contact__value--link::before { color: var(--ink); }
</style>
</head>
<body>
<div class="canvas">
  <section class="card card--front">
    <div class="card__pattern" role="img" aria-label="Faint network of connected nodes with white gears on the right"></div>
    <span class="brand-dot"></span>
    <div class="brand-name">VELIRO</div>
    <div class="tagline">Linking Partners - Shaping Flight</div>
  </section>

  <section class="card card--back">
    <div class="card__pattern" role="img" aria-label="Faint network of connected nodes with white gears on the right"></div>
    <span class="brand-dot"></span>
    <div class="brand-name">VELIRO</div>
    <div class="tagline">Linking Partners - Shaping Flight</div>
    <div class="person">
      <div class="person__name">Sample Name</div>
      <div class="person__role">Manager</div>
    </div>
    <ul class="contact">
      <li><span class="contact__label">Address</span><span class="contact__value">99 Lorem ipsum dolor sot amet</span></li>
      <li><span class="contact__label">Phone</span><span class="contact__value">9999 999 999</span></li>
      <li><span class="contact__label">Email</span><span class="contact__value contact__value--link">loremipsum@lorem.com</span></li>
      <li><span class="contact__label">Website</span><span class="contact__value contact__value--link">loremipsum.com</span></li>
    </ul>
  </section>
</div>
</body>
</html>
```